Add Responsiveness to Current Website

The website http://www.quillbrook-sound-rooms.example needs to be made responsive. This includes all the menus and all the galleries. The Design, graphics, colors can remain the same, except I can provide larger images and design for the Home Page. If you know what you are doing, this should not take too long.

Coding

Coded - Design and coding required

Number of Pages Required

5+ page

Font styles to use
Sans Serif

Colors
f37122
f78f20

Requirements
Must have
• Responsive Menus and Galleries

```html
<!DOCTYPE html>
<html lang="en">
<head>
<meta charset="utf-8">
<title>Quillbrook – Home Theater Design</title>
<link href="https://fonts.googleapis.com/css2?family=Open+Sans:wght@300;400;600;700&family=Cinzel:wght@700&display=swap" rel="stylesheet">
<style>
  :root{
    --page:#1e1e1e;
    --header:#2a221c;
    --text:#f2f2f2;
    --heading:#b8763c;
    --gold:#c9a25a;
    --rule:#444;
    --widget:#4b4b4b;
    --widget-card:#ffffff;
    --link:#2a4fa8;
    --star:#e8b321;
    --accent:#f37122;
  }
  *{margin:0;padding:0;box-sizing:border-box}
  html,body{width:1035px;height:1200px;overflow:hidden}
  body{position:relative;background:var(--page);color:var(--text);font-family:"Open Sans",Arial,sans-serif}

  .site-header{position:absolute;left:0;top:0;width:1035px;height:77px;
    background:linear-gradient(90deg,#3a2c20 0%,#1c1713 30%,#2b2219 70%,#4a3722 100%)}
  .brand{position:absolute;left:110px;top:14px;display:flex;align-items:center;gap:8px;
    font-family:"Open Sans",Arial,sans-serif;font-weight:700;font-size:30px;color:var(--gold)}
  .brand-dot{width:12px;height:12px;border-radius:50%;background:var(--gold)}
  .main-nav a{position:absolute;top:26px;font-size:12px;color:#fff;text-decoration:none;white-space:nowrap}
  .main-nav a.current::after{content:"";position:absolute;left:-3px;right:-3px;top:24px;height:3px;background:#fff}

  .hero{position:absolute;left:0;top:77px;width:1035px;height:341px;
    background:radial-gradient(ellipse at 50% 60%,#1b2540 0%,#0d1020 45%,#050507 100%)}
  .hero-title{position:absolute;left:0;width:1035px;text-align:center;font-family:"Cinzel",Georgia,serif;font-weight:700}
  .hero-title.line1{top:14px;font-size:46px;letter-spacing:27px;color:#efe9dc}
  .hero-title.line2{top:68px;font-size:50px;letter-spacing:24px;color:#b48a52}
  .hero-title.line3{top:126px;font-size:50px;letter-spacing:24px;color:#b48a52}

  .intro-title,.consult-title{position:absolute;font-weight:300;font-size:20px;color:var(--heading)}
  .intro-title{left:109px;top:476px}
  .consult-title{left:540px;top:872px}
  .copy{position:absolute;font-size:11.4px;line-height:17.5px}
  .copy p{margin-bottom:9px}
  .intro-copy{left:109px;top:532px;width:530px}
  .consult-copy{left:540px;top:928px;width:380px}

  .share{position:absolute;left:684px;top:478px;display:flex;gap:7px}
  .share span{width:24px;height:24px;border-radius:2px}
  .share .s1{background:#3b5998}.share .s2{background:#1da1f2}.share .s3{background:#dd4b39}.share .s4{background:#cb2027}

  .reviews{position:absolute;left:684px;top:524px;width:171px;height:243px;background:var(--widget);padding:5px}
  .reviews-head{display:flex;gap:5px;height:36px;align-items:center}
  .reviews-icon{width:28px;height:28px;background:#e7e7e7;border-radius:3px}
  .reviews-head strong{display:block;font-size:10.5px;color:#fff}
  .reviews-head small{font-size:8.5px;color:#fff}
  .reviews-list{background:var(--widget-card);margin-top:4px;border-radius:3px;padding:2px 4px}
  .review{border-bottom:1px solid #ddd;padding:4px 0;color:#333;font-size:8px;line-height:10px}
  .review:last-child{border-bottom:0}
  .review b{font-size:8.4px;color:#222}
  .review .stars{color:var(--star)}
  .review .more{color:var(--link);text-decoration:underline}
  .review .by{color:var(--link);font-size:7.5px;margin-top:2px}
  .badge{width:120px;height:12px;margin:6px auto 0;background:#fff;border-radius:6px;border:1px solid #f78f20}

  .divider{position:absolute;left:109px;top:828px;width:817px;height:1px;background:var(--rule)}
  .to-top{position:absolute;left:1006px;top:836px;width:29px;height:29px;background:#111}

  .consult-photo{position:absolute;left:109px;top:874px;width:386px;height:295px;
    background:linear-gradient(180deg,#7b6a7a 0%,#c88a5c 35%,#a6512c 65%,#4a2b1a 100%)}
</style>
</head>
<body>
  <header class="site-header">
    <div class="brand"><span class="brand-dot"></span>Quillbrook</div>
    <nav class="main-nav">
      <a class="current" style="left:341px">Home</a>
      <a style="left:391px">Products</a>
      <a style="left:453px">Gallery</a>
      <a style="left:507px">Let's Begin</a>
      <a style="left:577px">Acoustics</a>
      <a style="left:643px">Press</a>
      <a style="left:688px">Hospitality</a>
      <a style="left:759px">Our Story</a>
      <a style="left:826px">Seating</a>
      <a style="left:880px">Contact</a>
    </nav>
  </header>

  <section class="hero" role="img" aria-label="Home theater room with starfield wall panels, sconces and leather seating">
    <div class="hero-title line1">HOME THEATER</div>
    <div class="hero-title line2">Art &amp;</div>
    <div class="hero-title line3">Design</div>
  </section>

  <h2 class="intro-title">Home Theater Design</h2>
  <div class="copy intro-copy">
    <p>In terms of design, your Home Theater is the most versatile room in your home. Your options are limitless. You can compliment your existing home decor or you can create a design that is completely different from the rest of your home.</p>
    <p>If you enjoy exploring unique design opportunities, our decorative acoustic panels can act as a canvas for your inspiration.</p>
    <p>Ellis Marlow created dozens of original artistic designs specifically for Home Theater Interiors.</p>
    <p>Perhaps, you perfer a theme for your Home Theater Design. If so, we have designed theaters devoted to Outer Space, Wine, Sports, Music, Skylines, Secret Agent, Red Woods (and other landscapes) and more.</p>
    <p>Call Ellis today to discuss any of your Home Theater or Acoustic Panel needs and ask about our complimentary rendering services.</p>
  </div>

  <div class="share" aria-label="Share buttons"><span class="s1"></span><span class="s2"></span><span class="s3"></span><span class="s4"></span></div>

  <aside class="reviews">
    <div class="reviews-head">
      <span class="reviews-icon"></span>
      <div><strong>20 Customer Reviews</strong><small>Average Rating: <span style="color:var(--star)">★★★★★</span></small></div>
    </div>
    <div class="reviews-list">
      <div class="review"><span class="stars">★★★★★</span> <b>I reviewed the summary</b><br>Ellis and Quillbrook exceeded our expectations as we desi... <span class="more">(Read More)</span><div class="by">By Dana R Fairhaven, FL on 07/23/14</div></div>
      <div class="review"><span class="stars">★★★★★</span> <b>Oustanding service a ...</b><br>My wife chose these panels as an anniversary gift for me... <span class="more">(Read More)</span><div class="by">By Owen P Lakemont, TX on 03/02/14</div></div>
      <div class="review"><span class="stars">★★★★★</span> <b>Very happy!</b><br>I was looking for acoustic panels for our media room and want... <span class="more">(Read More)</span><div class="by">By Carla T Brookfield, IN on 12/22/12</div></div>
    </div>
    <div class="badge"></div>
  </aside>

  <div class="divider"></div>
  <div class="to-top"><svg width="29" height="29" viewBox="0 0 29 29"><path d="M9 17 L14.5 11.5 L20 17" fill="none" stroke="#fff" stroke-width="2"/></svg></div>

  <div class="consult-photo" role="img" aria-label="Theater wall with canyon landscape panels, sconces and leather recliners"></div>
  <h2 class="consult-title">You Personal Consultant</h2>
  <div class="copy consult-copy">
    <p>The moment you contact Quillbrook, you will talk directly with Ellis Marlow, the President and founder of the company. You will continue this personal dialog with Ellis throughout the entire process of designing your Home Theater.</p>
    <p>An effective home theater showcases your individuality. It is, well, very human. The customization process requires a relationship that is both professional and personal.</p>
    <p>Sometimes it will only take a few emails or phone conversations to finalize a design. Other times, it may take a great deal of time to design your ultimate Home Theater. Either way, will patiently work with you until you are 100% satisfied with your final design concept.</p>
  </div>
</body>
</html>
```